I want both print and ebook covers

book title is "The Classroom MEETING HANDBOOK: Fresh Paths to Partner With Families For Pupil Growth. I want a dark Teal or Navy Background. Yellow and white letters. Distorted Picture of one teacher, two parents and one child around a table or desk. But no Martians! My name should include "Award Winning Author"

Target Market(s)

teachers and other educators--principals, school psychologists, speech therapists, etc.

Industry/Entity Type

schools

• I just need to see how it looks

Colors
0054AA
0677BA
7BADD7
CADEEF
E8F1F8
0094D4
00A9DD
6FCCEA
C7EBF8
E9F6FB
FFC000
F8CF3A
FAE287
FDF2CF
FEFAEE

Requirements
Must have
• Title top third of page big enough to be read when reduced greatly in size. Contrast so that it "pops'.
Nice to have
• Teacher, two parents and one child around a table/desk. My name should include 'Award winning author'

```html
<!DOCTYPE html>
<html lang="en">
<head>
<meta charset="utf-8">
<title>The Classroom Meeting Handbook – Cover</title>
<link href="https://fonts.googleapis.com/css2?family=Oswald:wght@400;500;600&display=swap" rel="stylesheet">
<style>
  :root {
    --stage: #e9e7e4;
    --navy: #0d4d96;
    --navy-deep: #083a78;
    --yellow: #f8cf3a;
    --sky: #0ea2d8;
    --sky-light: #6fccea;
    --white: #ffffff;
  }
  * { margin: 0; padding: 0; box-sizing: border-box; }
  html, body {
    width: 1200px; height: 720px; overflow: hidden;
    background: var(--stage);
  }
  .stage {
    width: 1200px; height: 720px;
    display: flex; align-items: center; justify-content: center;
  }
  .cover {
    position: relative;
    width: 476px; height: 680px;
    overflow: hidden;
    background: var(--navy);
    font-family: "Oswald", "Arial Narrow", sans-serif;
    text-transform: uppercase;
  }
  .cover-art { position: absolute; inset: 0; }
  .award-tag {
    position: absolute;
    left: 84px; top: 12px;
    padding: 2px 14px 3px;
    background: var(--sky);
    color: var(--white);
    font-size: 14px; font-weight: 500;
    letter-spacing: 0.06em;
    font-style: italic;
    transform: rotate(-8deg);
  }
  .author-name {
    position: absolute;
    left: 190px; top: 38px;
    color: var(--yellow);
    font-size: 29px; font-weight: 500;
    line-height: 1;
  }
  .title {
    position: absolute;
    left: 0; right: 0; top: 84px;
    text-align: center;
    line-height: 0.92;
  }
  .title-lead {
    display: block;
    color: var(--white);
    font-size: 64px; font-weight: 500;
  }
  .title-main {
    display: block;
    color: var(--yellow);
    font-size: 126px; font-weight: 600;
    margin-top: 6px;
  }
  .title-end {
    display: block;
    color: var(--yellow);
    font-size: 92px; font-weight: 500;
    margin-top: 4px;
  }
  .subtitle {
    position: absolute;
    left: 0; right: 0; top: 430px;
    text-align: center;
    color: var(--sky-light);
    font-size: 24px; font-weight: 400;
    line-height: 1.2;
  }
</style>
</head>
<body>
<main class="stage">
  <article class="cover">
    <svg class="cover-art" width="476" height="680" viewBox="0 0 476 680">
      <defs>
        <linearGradient id="sceneTone" x1="0" y1="0" x2="0" y2="1">
          <stop offset="0" stop-color="#0a4a92"/>
          <stop offset="1" stop-color="#0d63b0"/>
        </linearGradient>
      </defs>
      <rect width="476" height="680" fill="var(--navy)"/>
      <g class="meeting-scene" role="img" aria-label="Illustration of a teacher, two parents and a child talking around a table">
        <rect x="0" y="500" width="476" height="180" fill="url(#sceneTone)"/>
        <ellipse class="table-top" cx="238" cy="712" rx="320" ry="84" fill="var(--sky)"/>
        <ellipse class="table-edge" cx="238" cy="700" rx="300" ry="66" fill="var(--sky-light)" opacity="0.35"/>
      </g>
      <path class="speech-bubble"
            d="M0 0 H462 L476 14 V404
               C452 440 420 470 392 492 L396 560 L352 530
               C300 552 240 560 180 556 C110 552 50 528 0 492 Z"
            fill="var(--navy-deep)"/>
    </svg>

    <div class="award-tag">Award Winning Author</div>
    <div class="author-name">Author’s Name</div>

    <h1 class="title">
      <span class="title-lead">The Classroom</span>
      <span class="title-main">Meeting</span>
      <span class="title-end">Handbook</span>
    </h1>

    <p class="subtitle">Fresh Paths to Partner With Families<br>For Pupil Growth</p>
  </article>
</main>
</body>
</html>
```